New Generation Winery needs inspiring label for special bottling

We are a family owned winery in the Rhine Valley in Germany. Check www.brandl-kohlmann.de . We have a very exciting project going: In 2014 we harvested our best vinyard and split the grapes in half. First half I have treated the way I have done it over the past 40 years. Second half I gave to my daughter who is just entering the winemaking business. She has treated it in a completely different way - her way - the way of the new generation. One of the differentiators; she has squeezed the juices with her bare feet which reduces acidity and bitterness in the wine (less tannins). This is why we want to call the wine "Kieselwind" (meaning "Pebblewind"). Please be careful when writing the "ß" . It is a German letter which replaces the "double s". It is NOT a capital B!! I Have attached a file which gives you the size of the label and another file which shows the current design of the winery labels. If possible it should pick up some elements from the current design (maybe just the colours?) but otherwise you are free. It will go on a dark green bottle, almost black. Apart from the word "Kieselwind" you need to place the grape "Riesling", the word "trocken" (means dry) and the year of the harvest "2014".

Industry/Entity Type

Brandl

Requirements
Nice to have
• Update 25.3.2015: Have a look at the attached image "Inspiration". Maybe that is a good thought starter, too. Have fun..

```html
<!DOCTYPE html>
<html lang="de">
<head>
<meta charset="utf-8">
<title>Brandl-Kohlmann Kieselwind Riesling</title>
<link rel="stylesheet" href="https://fonts.googleapis.com/css2?family=Cinzel:wght@600&family=Cormorant+Garamond:wght@500&family=Great+Vibes&display=swap">
<style>
  :root {
    --backdrop: #1b1b1c;
    --paper: #f1f0ee;
    --paper-edge: #e2e1de;
    --gold: #b8892e;
    --wine-red: #7a1a1e;
    --ink: #1f1a18;
    --script-brown: #5a1c1c;
  }
  * { margin: 0; padding: 0; box-sizing: border-box; }
  html, body {
    width: 789px;
    height: 1200px;
    overflow: hidden;
    background: var(--backdrop);
  }
  .label {
    position: absolute;
    left: 100px;
    top: 159px;
    width: 589px;
    height: 882px;
    background: radial-gradient(ellipse at 50% 45%, var(--paper) 60%, var(--paper-edge) 100%);
    text-align: center;
    color: var(--ink);
  }
  .label__rule {
    position: absolute;
    left: 0;
    right: 0;
    height: 4px;
    border-top: 2px solid var(--gold);
    border-bottom: 1px solid var(--gold);
  }
  .label__rule--top { top: 10px; }
  .label__rule--bottom { bottom: 10px; }
  .label__brand {
    position: absolute;
    top: 170px;
    left: 0;
    right: 0;
    font-family: "Cinzel", serif;
    font-weight: 600;
    font-size: 50px;
    letter-spacing: 0;
    color: var(--wine-red);
  }
  .label__name {
    position: absolute;
    top: 275px;
    left: 0;
    right: 0;
    font-family: "Cormorant Garamond", serif;
    font-weight: 500;
    font-size: 92px;
    color: var(--ink);
  }
  .label__grape {
    position: absolute;
    top: 430px;
    left: 0;
    right: 0;
    font-family: "Great Vibes", cursive;
    font-size: 170px;
    line-height: 1.2;
    color: var(--script-brown);
  }
  .label__style {
    position: absolute;
    top: 725px;
    left: 0;
    right: 0;
    font-family: "Cormorant Garamond", serif;
    font-weight: 500;
    font-size: 40px;
    letter-spacing: 2px;
    color: var(--ink);
  }
  .label__vintage {
    position: absolute;
    top: 785px;
    left: 0;
    right: 0;
    font-family: "Cormorant Garamond", serif;
    font-weight: 500;
    font-size: 50px;
    color: var(--ink);
  }
</style>
</head>
<body>
  <main class="label">
    <div class="label__rule label__rule--top"></div>
    <p class="label__brand">BRANDL-KOHLMANN</p>
    <h1 class="label__name">Kieselwind</h1>
    <p class="label__grape">Riesling</p>
    <p class="label__style">TROCKEN</p>
    <p class="label__vintage">2014</p>
    <div class="label__rule label__rule--bottom"></div>
  </main>
</body>
</html>
```